This Magazine is targeting White and African Americans women from 20 to 50 years of age.

GOSSIP , RELATIONSHIPS, BEAUTY, FASHION, WIGS AND HAIR WEAVE. NAILS , SALONS,

Community magazine targeting African Americans from 20 to 50 years of age.
Must be 8 pages.
Would like to have this art work don’t in PowerPoint or word doc
Must be bleed. Ready. for print double sided ,
Must have relationship section
must have gossip section..
must have
Must have a employment section.
Must have your own made-up coupons graffics with up 412 phone number
Must be in power-point bleed ready
I must be able to switch out coupons. with real one the customer gives me
This paper size I’m using is 12x 18 flip in half. 9x12

Make the name of the magazine called Sun Porch monthly magazine.

MUST HAVE BUSINESS SPOTLIGHT SECTION

THE COUPONS THAT I HAVE UP LOADED IS JUST HOW I WOULD LIKE THE MAGAZINE ADS TO LOOK . HOWEVER ALOT OF THEM SHOULD BE COUPONS FOR WOMEN NOT ALL BUT 70% OF THEM. I STILL WANT TO HAVE BUSINESS SUCH AS

AUTO REPAIR COUPONS
CHIROPRACTORS COUPON
DENTIST COUPONS
FLOWER SHOP COUPON
TEETH WHITING COUPON ,,,ETC

Target Market(s)

Colors
0094D4
00A9DD
6FCCEA
C7EBF8
E9F6FB
FFC000
F8CF3A
FAE287
FDF2CF
FEFAEE
E54698
E96AAD
F1A4CE
F9D9EA
FCEFF6

Requirements
Must have
• Sun Porch monthly Magazine 8 pages long..This Magazine is targeting White and African Americans women from 20 to 50 years of age. Would like to have this art work don’t in PowerPoint or word doc Must be bleed. Ready. for print double sided , Must have a employment section. Must have your own made-up coupon with up 412 phone number I must be able to witch out coupons. with real one the customer gives me This paper size I’m using is 12x 18 flip in half. 9x12 Make the name of the magazine called Sun Porch monthly magazine. MUST HAVE BUSINESS SPOTLIGHT SECTION ,MUST HAVE A HELP WANTED SECTION, and relationship section

```html
<!DOCTYPE html>
<html lang="en">
<head>
<meta charset="utf-8">
<title>Sun Porch monthly magazine – cover</title>
<link rel="stylesheet" href="https://fonts.googleapis.com/css2?family=Montserrat:wght@700;800;900&family=Lato:wght@300;400;700&family=Playfair+Display:wght@400&family=Great+Vibes&display=swap">
<style>
  :root{
    --stage:#e6e6e6;
    --paper:#ffffff;
    --ink:#0b0b0b;
    --magenta:#c0134f;
    --magenta-bright:#ec2a8c;
    --pink-text:#e0357a;
    --yellow:#d5b812;
    --quote:#e8d98a;
    --cover-grey:#e2e1df;
    --photo-warm-a:#bfb2a8;
    --photo-warm-b:#e6dfd7;
    --caption:#a9a9a9;
    --icon:#bdbdbd;
  }
  *{box-sizing:border-box;margin:0;padding:0}
  html,body{width:1200px;height:2650px;overflow:hidden;background:var(--paper)}
  body{position:relative;font-family:"Lato",sans-serif;color:var(--ink)}

  .stage{position:absolute;left:0;top:0;width:1200px;height:1810px;background:var(--stage)}

  .cover{position:absolute;left:145px;top:205px;width:917px;height:1300px;overflow:hidden;
    background:linear-gradient(90deg,var(--cover-grey) 0 295px,transparent 295px),
               linear-gradient(160deg,var(--photo-warm-a),var(--photo-warm-b) 70%);}
  .cover-photo{position:absolute;left:295px;top:0;width:622px;height:1300px;
    background:radial-gradient(ellipse at 62% 22%,#a7775a 0 16%,#3b2a22 26%,transparent 40%),
               linear-gradient(170deg,#bcafa5,#e9e3dc 60%,#d9d1c8)}
  .frame{position:absolute;left:33px;top:38px;width:843px;height:1224px;border:2px solid var(--ink)}

  .masthead{position:absolute;left:34px;top:78px;font-family:"Montserrat",sans-serif;font-weight:900;
    font-size:138px;line-height:.86;letter-spacing:-6px;color:var(--magenta)}

  .side-note{position:absolute;left:18px;top:462px;transform:rotate(-90deg);transform-origin:left top;
    font-size:8px;color:#666;white-space:nowrap}

  .info-bar{position:absolute;left:33px;top:425px;width:843px;height:50px;display:flex;
    border:2px solid var(--ink);font-family:"Montserrat",sans-serif;font-weight:800;white-space:nowrap}
  .info-bar > div{display:flex;align-items:center}
  .info-date{width:204px;background:var(--cover-grey);justify-content:center;font-size:16px}
  .info-volume{width:195px;background:var(--ink);color:var(--pink-text);justify-content:center;font-size:16px}
  .info-web{flex:1;background:var(--cover-grey);padding-left:14px;gap:10px;font-size:14px;color:var(--magenta)}
  .handle{font-size:11px;color:var(--ink);display:flex;align-items:center;gap:4px}
  .handle i{display:inline-block;width:9px;height:9px;border-radius:50%;background:var(--magenta)}

  .hot-band{position:absolute;left:0;top:475px;width:876px;height:325px;background:var(--yellow)}
  .hot-title{position:absolute;left:60px;top:30px;font-family:"Montserrat",sans-serif;font-weight:900;font-size:98px;line-height:1;letter-spacing:-3px}
  .hot-sub{position:absolute;left:60px;top:122px;font-family:"Montserrat",sans-serif;font-weight:900;font-size:38px;letter-spacing:-.5px}
  .kicker{font-family:"Lato",sans-serif;font-weight:700;font-size:13px;letter-spacing:.6px;white-space:nowrap}
  .hot-band .kicker{position:absolute;left:60px;top:177px}
  .body-copy{font-size:14px;line-height:22px}
  .hot-band .body-copy{position:absolute;left:60px;top:200px;width:300px;color:#3a3310}
  .hot-quote{position:absolute;left:58px;top:250px;font-family:"Playfair Display",serif;font-size:62px;line-height:1;letter-spacing:-1px;white-space:nowrap}
  .quote-mark{position:absolute;font-family:"Playfair Display",serif;font-size:190px;line-height:1;color:var(--quote)}
  .quote-open{left:340px;top:140px}
  .quote-close{left:752px;top:668px}

  .photo{position:absolute}
  .photo-hat{left:433px;top:486px;width:415px;height:237px;border:2px solid #d9cf9a;
    background:linear-gradient(120deg,#8d8881,#d8d4ce 40%,#b9b3ab 70%,#5f5b57)}
  .photo-couple{left:433px;top:820px;width:415px;height:240px;border:3px solid var(--ink);
    background:linear-gradient(100deg,#3a2a20,#8a6a55 35%,#c9b6a6 55%,#5a4030 80%,#2f231c)}
  .photo-pearls{left:58px;top:1005px;width:310px;height:208px;
    background:linear-gradient(110deg,#2b2b30,#6a6468 40%,#c9b58f 55%,#3a3638)}

  .page-tag{position:absolute;height:48px;background:var(--ink);color:#fff;display:flex;align-items:center;
    justify-content:center;font-family:"Montserrat",sans-serif;font-weight:800;font-size:15px;letter-spacing:7px}
  .tag-3{left:675px;top:640px;width:173px}
  .tag-7{left:675px;top:980px;width:173px}
  .tag-8{left:80px;top:1213px;width:170px}

  .save-date{position:absolute;left:58px;top:800px;width:310px;height:500px;background:var(--magenta);color:#fff}
  .save-date h2{position:absolute;left:18px;top:22px;font-family:"Lato",sans-serif;font-size:58px;line-height:54px;font-weight:700;white-space:nowrap}
  .save-date h2 span{font-weight:300;display:block}
  .save-date .body-copy{position:absolute;left:18px;top:133px;width:285px;color:#f6dbe5}

  .sentiments{position:absolute;left:440px;top:1060px;font-family:"Montserrat",sans-serif;font-weight:900;font-size:52px;letter-spacing:-1px;white-space:nowrap}
  .sentiments em{font-family:"Great Vibes",cursive;font-style:normal;font-weight:400;font-size:70px;letter-spacing:0}
  .sent-kicker{position:absolute;left:428px;top:1146px}
  .sent-copy{position:absolute;left:428px;top:1172px;width:340px;color:#4a4642}
  .fine-print{position:absolute;right:44px;top:1266px;font-size:8px;color:#6a625c;white-space:nowrap}

  .caption{position:absolute;left:0;top:1722px;width:1200px;text-align:center;font-family:"Montserrat",sans-serif;
    font-weight:800;font-size:13px;letter-spacing:9px;color:var(--caption)}

  .module-icon{position:absolute;left:558px;top:1832px}

  .brand-mark{position:absolute;left:0;top:2150px;width:1200px;text-align:center;font-family:"Montserrat",sans-serif;
    font-weight:900;font-size:170px;line-height:.88;letter-spacing:-7px;color:var(--magenta-bright)}
</style>
</head>
<body>
  <div class="stage">
    <article class="cover">
      <div class="cover-photo" role="img" aria-label="Cover portrait of a woman in a white textured jacket"></div>
      <div class="frame"></div>

      <h1 class="masthead">Sun<br>Porch</h1>
      <p class="side-note">Business spotlight: local salons, page 5 · Help wanted, page 6</p>

      <div class="info-bar">
        <div class="info-date">23TH. APRIL 2023</div>
        <div class="info-volume">VOLUME XXVI</div>
        <div class="info-web">WWW.SUNPORCHMAG.COM
          <span class="handle"><i></i>@SunPorchMag</span>
          <span class="handle"><i></i>@SunPorchMag</span>
        </div>
      </div>

      <section class="hot-band">
        <div class="quote-mark quote-open">“</div>
        <h2 class="hot-title">#HOT</h2>
        <p class="hot-sub">BUT SPOTLESS</p>
        <p class="kicker">GOSSIP · WHO'S TALKING THIS MONTH</p>
        <p class="body-copy">Salon chatter, wig and weave trends, and the nail looks everyone wants.</p>
        <p class="hot-quote">THEY KNOW YOUR SECRETS</p>
      </section>
      <div class="photo photo-hat" role="img" aria-label="Black and white photo of a woman in a wide-brim hat"></div>
      <div class="page-tag tag-3">PAGE 3</div>
      <div class="quote-mark quote-close">”</div>

      <section class="save-date">
        <h2>SAVE<span>THE DATE</span></h2>
        <p class="body-copy">Clip coupons for salons, nails and teeth whitening. Call 412-555-0148.</p>
      </section>
      <div class="photo photo-pearls" role="img" aria-label="Photo of a blonde woman in a black hat and pearl necklace"></div>
      <div class="page-tag tag-8">PAGE 8</div>

      <div class="photo photo-couple" role="img" aria-label="Photo of a smiling couple facing each other"></div>
      <div class="page-tag tag-7">PAGE 7</div>
      <h2 class="sentiments">SENT<em>iments!</em></h2>
      <p class="kicker sent-kicker">RELATIONSHIPS · LOVE &amp; LIFE</p>
      <p class="body-copy sent-copy">Real talk on dating, marriage and keeping the spark alive at any age.</p>
      <p class="fine-print">Coupons inside · Call 412-555-0148 · Employment listings page 6</p>
    </article>

    <p class="caption">4 OFFERS MODULAR LAYOUT</p>
  </div>

  <svg class="module-icon" width="84" height="116" viewBox="0 0 84 116" aria-label="Modular layout diagram">
    <rect x="1" y="1" width="82" height="114" rx="10" fill="#fff" stroke="#e2e2e2" stroke-width="2"/>
    <rect x="42" y="5" width="37" height="36" rx="9" fill="var(--icon)"/>
    <rect x="5" y="45" width="74" height="26" rx="9" fill="var(--icon)"/>
    <rect x="5" y="75" width="35" height="36" rx="9" fill="var(--icon)"/>
    <rect x="44" y="75" width="35" height="36" rx="9" fill="var(--icon)"/>
  </svg>

  <p class="brand-mark">Sun<br>Porch</p>
</body>
</html>
```